Theatre Company needs a Poster design for a world premiere of "Ember Hollow" Play.

We are premiering a play that celebrates community in rural and regional Australia . We need a poster for A3 and A5 size and an image that can be used in our email correspondence/webpage.

Attached is some ideas the producing theatre committee has come up with, a river runs through the town itself.

Town

```html
<!DOCTYPE html>
<html lang="en">
<head>
<meta charset="utf-8">
<title>Ember Hollow — Poster</title>
<link rel="stylesheet" href="https://fonts.googleapis.com/css2?family=Bodoni+Moda:opsz,wght@6..96,400;6..96,500&family=Playfair+Display:wght@400;500&display=swap">
<style>
  :root {
    --night: #111214;
    --night-mid: #3c3f44;
    --night-glow: #b9bcc0;
    --crimson: #8a0d1c;
    --crimson-light: #b4202f;
    --crimson-glow: #c0303c;
    --crimson-deep: #780a17;
    --ivory: #f6f1ee;
  }
  * { margin: 0; padding: 0; box-sizing: border-box; }
  html, body {
    width: 849px;
    height: 1200px;
    overflow: hidden;
    background: var(--night);
  }
  .poster {
    position: relative;
    width: 849px;
    height: 1200px;
    overflow: hidden;
  }
  .poster__photo {
    position: absolute;
    inset: 0;
    background:
      radial-gradient(ellipse 14% 22% at 2% 50%, var(--night-glow) 0%, transparent 80%),
      radial-gradient(ellipse 16% 24% at 99% 50%, var(--night-glow) 0%, transparent 80%),
      radial-gradient(ellipse 10% 30% at 3% 76%, #7c7f84 0%, transparent 80%),
      radial-gradient(ellipse 10% 30% at 98% 76%, #8b8e93 0%, transparent 80%),
      linear-gradient(180deg, var(--night) 0%, var(--night) 34%, var(--night-mid) 44%, #55585d 58%, var(--night-mid) 72%, #1c1d20 90%, var(--night) 100%);
  }
  .poster__panel {
    position: absolute;
    left: 50px;
    top: 53px;
    width: 748px;
    height: 1095px;
    background:
      radial-gradient(ellipse 30% 12% at 62% 44%, var(--crimson-glow) 0%, transparent 80%),
      radial-gradient(ellipse 18% 26% at 94% 48%, #d04452 0%, transparent 80%),
      radial-gradient(ellipse 60% 22% at 45% 72%, var(--crimson-light) 0%, transparent 80%),
      radial-gradient(ellipse 40% 10% at 30% 42%, #a01828 0%, transparent 80%),
      linear-gradient(180deg, var(--crimson) 0%, var(--crimson) 36%, #951424 52%, #9c1828 70%, var(--crimson) 86%, var(--crimson-deep) 100%);
  }
  .poster__presenter,
  .poster__credit {
    position: absolute;
    font-family: "Playfair Display", serif;
    font-weight: 500;
    font-size: 14px;
    letter-spacing: 0.01em;
    text-transform: uppercase;
    color: var(--ivory);
    white-space: nowrap;
  }
  .poster__presenter { left: 84px; top: 313px; }
  .poster__credit { right: 81px; top: 594px; }
  .poster__title {
    position: absolute;
    left: 0;
    top: 0;
    width: 849px;
    height: 1200px;
  }
  .poster__title .title-line {
    font-family: "Bodoni Moda", serif;
    font-weight: 400;
    font-variation-settings: "opsz" 96;
    fill: var(--ivory);
  }
  .poster__title .tagline {
    font-family: "Playfair Display", serif;
    font-weight: 400;
    fill: var(--ivory);
  }
</style>
</head>
<body>
  <main class="poster">
    <div class="poster__photo" role="img" aria-label="Night photograph of an arched town bridge over a river, lamps reflected in the water"></div>
    <div class="poster__panel" role="img" aria-label="Bridge arches and river reflections seen through a crimson tint"></div>

    <p class="poster__presenter">Wattle Bend Theatre Company presents to you</p>
    <p class="poster__credit">Written by Dara Whitlock</p>

    <svg class="poster__title" viewBox="0 0 849 1200" aria-label="Ember Hollow">
      <text class="title-line" x="80" y="500" font-size="200" textLength="600" lengthAdjust="spacingAndGlyphs">EMBER</text>
      <text class="title-line" x="80" y="782" font-size="200" textLength="688" lengthAdjust="spacingAndGlyphs">HOLLOW</text>
      <text class="tagline" x="84" y="828" font-size="37" textLength="672" lengthAdjust="spacingAndGlyphs">“a river runs through the town itself”</text>
    </svg>
  </main>
</body>
</html>
```